Modern Social Media Ad for Law Firm

We need a crisp ad for social media for our law firm, The Hargrove Firm. The ad will adverrtise for car accident and personal injury cases. Our website is rightsforyouexample.com. Our phoone number is 555-314-8826. Use a photo of of our building in the background. I want the add to be light and cripsy. Use logo and photo of attorney. Our address is 718 North Birch Avenue at Red Marlin Ballpark.

Target Market(s)

We want to car accident cases and injury cases. The ad should say "Car Accident or Injury? Call us." No fee unless we win!

Industry/Entity Type

Legal

Requirements
Must have
• large photo of me. white background. maybe grayed out columns in the background. website at the bottom with phone number. The Hargrove Firm logo and name at top. Our colors are black and gold with red as an accent color. Should say "Pensacola, FL" at the bottom in small print.
Nice to have
• if you could fade our building into the background that woul dbe nice
Should not have
• no scales of justice -- I want it to be clean, white, crisp, modern

```html
<!DOCTYPE html>
<html lang="en">
<head>
<meta charset="utf-8">
<title>The Hargrove Firm – Car Accident or Injury Ad</title>
<link href="https://fonts.googleapis.com/css2?family=Oswald:wght@300;400;500;600&family=Cormorant+Garamond:wght@500&display=swap" rel="stylesheet">
<style>
  :root {
    --stage: #2a2a2a;
    --paper: #ffffff;
    --ink: #161616;
    --gold: #d69e2e;
    --fade-light: #f2f2f2;
    --fade-mid: #d9d9d9;
    --suit-light: #8a8d92;
    --suit-dark: #55585d;
    --white: #ffffff;
  }
  * { margin: 0; padding: 0; box-sizing: border-box; }
  html, body {
    width: 1200px; height: 900px; overflow: hidden;
    background: var(--stage);
  }
  .ad {
    position: absolute; left: 300px; top: 26px;
    width: 600px; height: 848px;
    background: var(--paper);
    overflow: hidden;
    font-family: "Oswald", "Arial Narrow", sans-serif;
    color: var(--ink);
  }
  .building-photo {
    position: absolute; left: 0; top: 125px; width: 600px; height: 600px;
    background: linear-gradient(180deg, var(--paper) 0%, var(--fade-light) 30%, var(--fade-mid) 70%, var(--fade-light) 100%);
    opacity: .85;
  }
  .attorney-photo {
    position: absolute; left: 282px; top: 44px; width: 318px; height: 804px;
    background: linear-gradient(180deg, #e9e9e9 0%, var(--suit-light) 30%, var(--suit-dark) 100%);
  }
  .brand {
    position: absolute; left: 40px; top: 40px; width: 200px;
    text-align: center;
  }
  .brand-mark {
    width: 72px; height: 72px; margin: 20px auto 22px;
    background: var(--gold);
  }
  .brand-name {
    font-size: 15px; font-weight: 500; letter-spacing: .5px;
    text-transform: uppercase; color: var(--ink);
  }
  .brand-tagline {
    font-family: "Cormorant Garamond", Georgia, serif;
    font-size: 11px; color: var(--ink);
    border-top: 1px solid var(--ink); border-bottom: 1px solid var(--ink);
    display: inline-block; padding: 0 18px; line-height: 12px;
  }
  .headline {
    position: absolute; left: 46px; top: 262px;
    font-size: 58px; font-weight: 500; line-height: 57px;
    text-transform: uppercase; letter-spacing: -.5px;
  }
  .headline .cta { color: var(--gold); display: block; }
  .promise {
    position: absolute; left: 46px; top: 472px;
    font-size: 23px; font-weight: 500; line-height: 28px;
    text-transform: uppercase;
  }
  .address {
    position: absolute; left: 46px; top: 628px;
    font-size: 19px; font-weight: 500; line-height: 28px;
  }
  .phone {
    position: absolute; left: 44px; top: 680px;
    font-size: 94px; font-weight: 500; line-height: 110px;
    color: var(--gold); letter-spacing: -1px;
  }
  .website {
    position: absolute; left: 46px; top: 795px;
    font-size: 27px; font-weight: 300;
  }
  .locale {
    position: absolute; left: 494px; top: 808px;
    font-size: 11px; font-weight: 300; color: var(--white);
  }
</style>
</head>
<body>
  <main class="ad">
    <div class="building-photo" role="img" aria-label="Faded black-and-white photo of the firm's building in the background"></div>
    <div class="attorney-photo" role="img" aria-label="Photo of the attorney in a grey suit and teal tie, arms folded"></div>

    <header class="brand">
      <div class="brand-mark"></div>
      <div class="brand-name">The Hargrove Firm, PLLC.</div>
      <div class="brand-tagline">Attorneys At Law</div>
    </header>

    <h1 class="headline">
      Car Accident<br>or Injury?
      <span class="cta">Call Us.</span>
    </h1>

    <p class="promise">No fee unless<br>we win!</p>

    <p class="address">718 North Birch Avenue<br>at Red Marlin Ballpark</p>

    <p class="phone">555-314-8826</p>
    <p class="website">rightsforyouexample.com</p>
    <p class="locale">Pensacola, FL</p>
  </main>
</body>
</html>
```